TrevanHollis's Signature Beard Oil Label Design

I'm looking for a creative designer to run with the design. I am not sure what I really want so surprise me. What ever you do please use earth tone colors. The bottles I use is 2.0 ounces. It is a Boston amber bottle with glass dropper. It is 1.5 width by 3.75 inch height. :Benefits : * Organic * Hair growth* Repairs Split Ends* Softens * Health Shine* Aromatherapy fragrance* Reduce Itching/Irritation * Reduce Dandruff* Reduces Flyaway hair Directions: Place a nickel size drop into palm of handMassage into beard 2 to 3 times a day

Target Market(s)

MEN WITH BEARDS AND MEN THAT WANT TO GROW BEARDS BUT DON'T KNOW HOW

Industry/Entity Type

Hair Care Product

Font styles to use
Serif
Script

Colors
1b1b1b
fdf9cf
ffc214
ffffff

Requirements
Must have
• FALL COLOR SCHEME, Trevan Hollis written in a fancy cursive script, all others can me different, please use the gold lion logo without the word Lion.
Nice to have
• CLASSY, MANLY, OLD AND NEW SCHOOL ESSENCE
Should not have
• Anything feminine, Flint Cove

```html
<!DOCTYPE html>
<html lang="en">
<head>
<meta charset="utf-8">
<title>Trevan Hollis Beard Oil Label</title>
<link rel="stylesheet" href="https://fonts.googleapis.com/css2?family=Noticia+Text:ital,wght@1,700&family=Pinyon+Script&display=swap">
<style>
  :root {
    --ink: #1b1b1b;
    --cream: #fdf9cf;
    --gold: #ffc214;
    --gold-deep: #e0a810;
    --white: #ffffff;
    --label-grey: #a6a6a6;
    --serif: "Noticia Text", Georgia, serif;
    --script: "Pinyon Script", cursive;
  }
  * { margin: 0; padding: 0; box-sizing: border-box; }
  html, body { width: 689px; height: 1200px; overflow: hidden; background: var(--white); }
  .sheet { position: relative; width: 689px; height: 1200px; background: var(--white); }

  .palette { position: absolute; left: 0; top: 242px; }
  .swatch {
    width: 87px; height: 34px; margin-bottom: 15px;
    border: 1.5px solid var(--ink);
  }
  .swatch--ink { background: var(--ink); }
  .swatch--cream { background: var(--cream); }
  .swatch--gold { background: var(--gold); }

  .label {
    position: absolute; left: 209px; top: 0;
    width: 480px; height: 1200px;
    background: var(--label-grey);
    color: var(--ink);
  }
  .mascot {
    position: absolute; left: 46px; top: 203px;
    width: 300px; height: 276px;
  }
  .brand-name {
    position: absolute; left: 150px; top: 334px;
    font-family: var(--script); font-weight: 400;
    font-size: 74px; line-height: 70px;
    color: var(--ink);
    white-space: nowrap;
  }
  .brand-name span { display: block; }
  .brand-name span + span { padding-left: 22px; }

  .product-name {
    position: absolute; left: 60px; top: 484px; width: 370px;
    text-align: center;
    font-family: var(--script); font-weight: 400;
    font-size: 82px; line-height: 90px;
    color: var(--ink);
    white-space: nowrap;
  }
  .benefits {
    position: absolute; left: 38px; top: 574px;
    list-style: none;
    font-family: var(--serif); font-style: italic; font-weight: 700;
    font-size: 31px; line-height: 32.4px;
  }
  .benefits li { position: relative; padding-left: 20px; white-space: nowrap; }
  .benefits li::before {
    content: ""; position: absolute; left: 2px; top: 16px;
    width: 7px; height: 7px; background: var(--ink);
    border-radius: 0 50% 50% 50%; transform: rotate(45deg);
  }
  .directions {
    position: absolute; left: 38px; top: 838px; width: 440px;
    font-family: var(--serif); font-style: italic; font-weight: 700;
    font-size: 31px; line-height: 30px;
    white-space: nowrap;
  }
</style>
</head>
<body>
<main class="sheet">
  <aside class="palette">
    <div class="swatch swatch--ink"></div>
    <div class="swatch swatch--cream"></div>
    <div class="swatch swatch--gold"></div>
  </aside>

  <section class="label">
    <svg class="mascot" viewBox="0 0 300 276" role="img" aria-label="Gold lion mascot illustration wearing a black bowler hat, with a flowing gold mane and dark beard">
      <defs>
        <linearGradient id="mascot-tone" x1="0" y1="0" x2="0" y2="1">
          <stop offset="0" stop-color="#ffc214"/>
          <stop offset="0.45" stop-color="#e0a810"/>
          <stop offset="1" stop-color="#1b1b1b"/>
        </linearGradient>
      </defs>
      <path d="M0,40 Q0,0 40,0 H270 Q300,0 300,30 V100 Q300,125 275,125 H110 Q94,125 94,141 V256 Q94,276 74,276 H20 Q0,276 0,256 Z" fill="url(#mascot-tone)"/>
    </svg>
    <h1 class="brand-name"><span>Trevan</span><span>Hollis</span></h1>
    <h2 class="product-name">Beard Oil</h2>
    <ul class="benefits">
      <li>Organic</li>
      <li>Hair growth</li>
      <li>Repairs Split Ends</li>
      <li>Softens</li>
      <li>Health Shine</li>
      <li>Aromatherapy fragrance</li>
      <li>Reduce Itching/Irritation</li>
    </ul>
    <p class="directions">Place a nickel size drop<br>into palm of hand Massage<br>beard 2 to 3 times a day</p>
  </section>
</main>
</body>
</html>
```